New boutique hotel for tourists, with hint of art deco styling

This is a new, soon to be completed, boutique hotel in Sydney. A letterhead with a logo is required. Less emphasis on the word "boutique". Perhaps the word could be screened to be lighter in colour (or print intensity). Would like a simple, clear, easy-to read, sans serif type face. The information on the letterhead is:
Mrs Perrow Boutique Hotel
418 Calloway Street,
Wrenfield, NSW, 2094
Australia
Tel: +61 2 9478-0000
mrsperrowhotel@example-mail.com
mrsperrowhotel.com.au
ABN 47 902 365 118

Target Market(s)

travellers, tourists, various ages

Industry/Entity Type

Hospitality

Contact Information for Business Card

Mrs Perrow Boutique Hotel
418 Calloway Street,
Wrenfield, NSW, 2094
Telephone: (02) 9478-0000
www.mrsperrowhotel.com.au
mrsperrowhotel@example-mail.com
ABN 47 902 365 118

Logo Text

suggest playing with the letter "B"

Font styles to use
Sans Serif

Colors
3176b5

Requirements
Must have
• ABN to be very small.
• Must be clear, easy to read and in a sans serif typeface, please!
Nice to have
• The word "Boutique" should be less intense in appearance to the rest of the name, or even "Boutique Hotel" can have less prominence than "Mrs Perrow".
Should not have
• No serif typeface. Sans serif only will be accepted.

```html
<!DOCTYPE html>
<html lang="en">
<head>
<meta charset="utf-8">
<title>Mrs Perrow Boutique Hotel – Letterhead</title>
<link href="https://fonts.googleapis.com/css2?family=Arimo:wght@700&family=Questrial&display=swap" rel="stylesheet">
<style>
  :root {
    --paper: #ffffff;
    --ink-grey: #9b9b9d;
    --ink-soft: #8c8c8e;
    --blush: #fdeeee;
    --blush-deep: #f6cfd2;
    --mark-dot: #f2a7b3;
  }
  html, body {
    margin: 0;
    padding: 0;
    width: 848px;
    height: 1200px;
    overflow: hidden;
    background: var(--paper);
  }
  .letterhead {
    position: relative;
    width: 848px;
    height: 1200px;
    background: var(--paper);
    overflow: hidden;
  }
  .brand {
    position: absolute;
    left: 44px;
    top: 76px;
    display: flex;
    align-items: center;
    gap: 14px;
  }
  .brand-dot {
    width: 22px;
    height: 22px;
    border-radius: 50%;
    background: var(--mark-dot);
    flex: none;
  }
  .brand-name {
    font-family: "Arimo", Arial, sans-serif;
    font-weight: 700;
    color: var(--ink-grey);
    line-height: 1;
  }
  .brand-name .line-main {
    display: block;
    font-size: 58px;
    letter-spacing: -1px;
  }
  .brand-name .line-sub {
    display: block;
    font-size: 26px;
    margin-top: 12px;
    padding-left: 28px;
  }
  .watermark {
    position: absolute;
    left: 163px;
    top: 313px;
    width: 500px;
    height: 500px;
  }
  .footer-band {
    position: absolute;
    left: 0;
    top: 997px;
    width: 848px;
    height: 203px;
    background: var(--blush);
  }
  .footer-name {
    position: absolute;
    left: 30px;
    top: 1024px;
    margin: 0;
    font-family: "Arimo", Arial, sans-serif;
    font-weight: 700;
    font-size: 33px;
    letter-spacing: -0.5px;
    color: var(--ink-grey);
  }
  .contact {
    position: absolute;
    margin: 0;
    font-family: "Questrial", Arial, sans-serif;
    color: var(--ink-soft);
    font-size: 20px;
    line-height: 29px;
    letter-spacing: -0.3px;
  }
  .contact-email { left: 31px; top: 1080px; font-size: 18px; }
  .contact-abn { left: 35px; top: 1138px; }
  .contact-address { left: 326px; top: 1080px; font-style: normal; }
  .contact-web { left: 600px; top: 1078px; }
  .contact-tel { left: 605px; top: 1137px; }
</style>
</head>
<body>
  <main class="letterhead">
    <header class="brand">
      <span class="brand-dot"></span>
      <span class="brand-name">
        <span class="line-main">Mrs Perrow</span>
        <span class="line-sub">Boutique Hotel</span>
      </span>
    </header>

    <svg class="watermark" viewBox="0 0 500 500" role="img" aria-label="Faint blush decorative motif behind the letter body">
      <defs>
        <radialGradient id="blushGlow" cx="50%" cy="50%" r="50%">
          <stop offset="0%" stop-color="#f6cfd2" stop-opacity="0.45"/>
          <stop offset="70%" stop-color="#fbe4e6" stop-opacity="0.3"/>
          <stop offset="100%" stop-color="#ffffff" stop-opacity="0"/>
        </radialGradient>
      </defs>
      <circle cx="250" cy="250" r="250" fill="url(#blushGlow)"/>
    </svg>

    <footer class="footer-band"></footer>
    <h2 class="footer-name">Mrs Perrow</h2>
    <p class="contact contact-email">mrsperrowhotel@example-mail.com</p>
    <p class="contact contact-abn">ABN 47 902 365 118</p>
    <address class="contact contact-address">418 Calloway Street<br>Wrenfield, NSW, 2094<br>Australia</address>
    <p class="contact contact-web">mrsperrowhotel.com.au</p>
    <p class="contact contact-tel">Tel: +61 2 9478-0000</p>
  </main>
</body>
</html>
```